Home Page Design (+50 More Pages To Winning Designer!)

We have a 50+ page website, but we're starting with the home page. The winning designer will get all 50+ pages to design as a 2nd project, so make sure you do your best!

SoarVane is in the private jet industry and needs a re-designed website.

We have created the structure for the website and content inside of Tavoni.io (THESE ARE ONLY ROUGH A.I. GENERATED WIREFRAMES AND DO NOT NEED TO BE FOLLOWED EXACTLY) - https://www.tavoni.io/app/project/P482915_qRuVwKsLm-DDtaHrYuop72XNc8fkoPzqlrhwDxHkaWm3Tq

Take the content from the 'Home Page' under the 'Wireframe' tab on the Tavoni.io link above, but feel free to re-design the page in a better way as these are only A.I. generated wireframes.

We want a DARK theme.... High quality, luxurious feel, greyscale colors. Attached is a brand guideline (BUT THIS IS NOT A 100% BRAND GUIDELINE, YOU CAN CHANGE COLORS AND FONTS AND MAKE CHANGES IF YOU HAVE BETTER IDEAS) and attached is our logo. We are also attaching some examples of other apps and websites to give you a guideline of what we're looking for for this design project.

The final design MUST communicate luxury using high-quality imagery of large cabin luxurious private jets.

ENTRIES THAT DO NOT FOLLOW THE PROJECT BRIEF WILL BE AUTOMATICALLY DISCARDED. FOLLOW THE INSTRUCTIONS!

Industry/Entity Type

Travel

Number of Pages Required

1 page

Font styles to use
Sans Serif

Colors

Designer to choose colors to be used in the design.

Requirements
Must have
• Follow wireframe and use content in wireframe (see Tavoni.io link)

```html
<!DOCTYPE html>
<html lang="en">
<head>
<meta charset="utf-8">
<title>SoarVane — Private Jet Programs</title>
<link href="https://fonts.googleapis.com/css2?family=Lexend:wght@300;400;500;600&display=swap" rel="stylesheet">
<style>
:root{
  --bg:#000;
  --panel:#0b0c0e;
  --line:#2a2c30;
  --green:#22e58c;
  --green-dim:#0f5f3b;
  --text:#f2f2f2;
  --muted:#a7a9ad;
}
*{box-sizing:border-box;margin:0;padding:0}
html,body{width:1200px;height:4563px;overflow:hidden}
body{background:var(--bg);color:var(--text);font-family:"Lexend",sans-serif;position:relative}
.abs{position:absolute}
.glow{position:absolute;border-radius:50%;background:radial-gradient(circle,rgba(34,229,140,.28),rgba(34,229,140,0) 68%);pointer-events:none}
.btn{display:flex;align-items:center;justify-content:center;background:var(--green);color:#03170d;border-radius:4px;font-weight:500}
.btn-outline{display:flex;align-items:center;justify-content:center;border:1.5px solid var(--green);color:var(--green);border-radius:4px;font-size:10px}
.kicker{position:absolute;left:0;width:1200px;text-align:center;color:var(--green);font-size:26px;letter-spacing:9px;font-weight:400}

/* nav */
.nav-logo{left:168px;top:40px;font-size:24px;font-weight:400;letter-spacing:-.5px}
.nav-links{left:330px;top:50px;display:flex;gap:24px;font-size:10.5px;letter-spacing:-.2px;color:#ddd;white-space:nowrap}
.nav-cta{left:913px;top:40px;width:119px;height:34px;font-size:10px}

/* hero */
.hero-photo{left:101px;top:115px;width:996px;height:434px;border-radius:6px;background:radial-gradient(ellipse at 50% 60%,#6a6c70,#2b2c2f 55%,#111 100%)}
.hero-title{left:101px;top:232px;width:996px;text-align:center;font-size:37px;line-height:42px;font-weight:400;letter-spacing:-.8px}
.hero-cta{left:541px;top:349px;width:118px;height:32px;font-size:12px;font-weight:600}

/* fractional */
.frac-title{left:0;top:628px;width:1200px;text-align:center;font-size:26px;font-weight:400;letter-spacing:-.6px}
.frac-title span{color:var(--green)}
.frac-copy{left:255px;top:672px;width:690px;text-align:center;font-size:11px;line-height:19.5px;letter-spacing:-.1px;color:#cfd0d2}
.frac-btn{left:540px;top:780px;width:119px;height:33px;z-index:2;background:#000}
.jet-one{left:195px;top:820px;width:877px;height:252px;background:radial-gradient(ellipse at 50% 55%,#3a3c40,#15161a 55%,rgba(0,0,0,0) 75%)}

/* features */
.cards{left:167px;top:1207px;display:grid;grid-template-columns:repeat(3,271px);gap:25px 26px}
.card{height:259px;border:1.5px solid #34373b;border-radius:8px;background:#060807;position:relative}
.card:first-child{border-color:#1e8f5b}
.card h3{position:absolute;left:22px;top:72px;font-size:13.5px;font-weight:500;line-height:16px;letter-spacing:.6px}
.card h3 em{font-style:normal;color:var(--green)}
.card p{position:absolute;left:22px;right:22px;top:128px;font-size:10.5px;line-height:17.5px;color:#bdbec1}
.card svg{position:absolute;right:28px;top:38px}

/* benefits */
.benefits{left:168px;top:1811px;width:864px;height:110px;border:1px solid #3a3c40;border-radius:8px;background:#121419}
.benefits h2{position:absolute;left:146px;top:40px;color:var(--green);font-size:25px;font-weight:400;letter-spacing:8px}
.benefits p{position:absolute;left:382px;top:45px;font-size:19px;font-weight:300;word-spacing:2px}
.jet-two{left:138px;top:1900px;width:1062px;height:395px;background:radial-gradient(ellipse at 40% 50%,#8a8c90,#3a3c40 40%,rgba(0,0,0,0) 72%)}

/* services */
.services{left:191px;top:2457px;display:grid;grid-template-columns:repeat(3,297px);row-gap:42px}
.service h4{display:flex;align-items:center;gap:10px;font-size:13px;font-weight:400}
.service h4 i{width:19px;height:19px;border-radius:4px;background:var(--green-dim);display:inline-block;position:relative}
.service h4 i::after{content:"";position:absolute;inset:5px;border-radius:50%;background:var(--green)}
.service p{margin-top:12px;width:225px;font-size:10.5px;line-height:16px;color:#aeb0b3}

.cta-box{left:168px;width:864px;height:110px;border:1.5px solid #1e8f5b;border-radius:8px;background:linear-gradient(90deg,#06140d,#030504)}
.cta-box p{position:absolute;left:40px;top:42px;font-size:20px;font-weight:300}
.cta-box .btn{position:absolute;right:38px;top:28px;width:181px;height:52px;font-size:19px;font-weight:400}

/* testimonial */
.orb{position:absolute;border-radius:50%;background:radial-gradient(circle at 40% 40%,#22e58c,#0c7a47 60%,#03301c)}
.quote-card{left:340px;top:2959px;width:530px;height:337px;border:1px solid #4a4c50;border-radius:8px;background:linear-gradient(180deg,rgba(90,92,96,.75),rgba(20,21,24,.9) 80%)}
.quote-mark{position:absolute;left:16px;top:-10px;font-size:120px;line-height:1;color:#8c8e92;font-weight:600}
.quote-text{position:absolute;left:24px;top:112px;width:460px;font-size:13.5px;line-height:20.5px;color:#e8e8e8}
.author{position:absolute;left:22px;top:272px;display:flex;align-items:center;gap:14px}
.author .avatar{width:50px;height:50px;border-radius:50%;background:linear-gradient(135deg,#5e5e60,#2a2a2c)}
.author b{display:block;font-size:11px;font-weight:400}
.author small{font-size:8.5px;color:#bbb}
.arrow{position:absolute;top:3324px;width:42px;height:42px;border-radius:50%;display:flex;align-items:center;justify-content:center}

/* partners */
.brands{left:0;top:3425px;width:1200px;height:103px;background:#111214;display:flex;align-items:center;justify-content:space-between;padding:0 167px;font-size:17px;color:#c9cacc;font-weight:400}

/* newsletter */
.newsletter{left:168px;top:3574px;width:864px;height:165px;border:1.5px solid #1e8f5b;border-radius:8px;background:linear-gradient(90deg,#0a2a1c,#06130d)}
.newsletter h2{position:absolute;left:40px;top:42px;font-size:23px;font-weight:400}
.newsletter p{position:absolute;left:40px;top:86px;width:320px;font-size:10.5px;line-height:17px;color:#9ea19f}
.email{position:absolute;left:470px;top:60px;width:334px;height:42px;border-radius:22px;background:#0a0c0b;border:1px solid #1c2a22}
.email span{position:absolute;left:18px;top:14px;font-size:11px;color:#bbb}
.email .btn{position:absolute;right:8px;top:6px;width:84px;height:30px;border-radius:16px;font-size:11px}

/* faq */
.faq{left:0;top:3789px;width:590px;height:358px;background:#0d0e10}
.faq-visual{left:590px;top:3789px;width:610px;height:358px;background:radial-gradient(ellipse at 50% 60%,#5a5c60,#1c1d20 55%,#08090a 90%)}
.faq h2{position:absolute;left:193px;top:50px;color:var(--green);font-size:25px;font-weight:400;letter-spacing:7px}
.faq-item{position:absolute;left:193px;width:428px;font-size:11px}
.faq-item .q{display:flex;justify-content:space-between;align-items:center;font-weight:500}
.faq-item .a{margin-top:10px;width:330px;font-size:9.5px;line-height:15px;color:#9fa1a4}

/* footer */
.footer-logo{left:213px;top:4402px;font-size:24px;font-weight:400}
.footer-links{left:453px;top:4411px;display:flex;gap:20px;font-size:10px;color:#8a8c90;white-space:nowrap}
.footer-rule{left:213px;top:4464px;width:783px;height:1px;background:#222}
.footer-copy{left:205px;top:4492px;font-size:9px;color:#8a8c90}
.status{left:550px;top:4486px;width:110px;height:22px;border:1px solid #2f3a34;border-radius:11px;font-size:8.5px;color:#bbb;display:flex;align-items:center;justify-content:center;gap:5px}
.status i{width:5px;height:5px;border-radius:50%;background:var(--green)}
.socials{left:843px;top:4491px;display:flex;gap:17px}
.socials i{width:14px;height:14px;border:1.5px solid #8a8c90;border-radius:3px;display:block}
</style>
</head>
<body>

<div class="glow" style="left:-200px;top:330px;width:500px;height:500px"></div>
<div class="glow" style="left:850px;top:840px;width:560px;height:560px"></div>
<div class="glow" style="left:420px;top:1560px;width:380px;height:380px"></div>
<div class="glow" style="left:-80px;top:1980px;width:520px;height:480px"></div>

<!-- navigation -->
<div class="abs nav-logo">SoarVane</div>
<nav class="abs nav-links"><span>Aircraft</span><span>Programs</span><span>Why SoarVane</span><span>Lifestyle</span><span>Sustainability</span><span>Resources</span><span>Competitors</span></nav>
<div class="abs btn-outline nav-cta">Contact Us</div>

<!-- hero -->
<div class="abs hero-photo" role="img" aria-label="Photo of a long private jet cabin interior with leather seats and oval windows"></div>
<h1 class="abs hero-title">Explore the different flight<br>programs with SoarVane</h1>
<div class="abs btn hero-cta">Contact Us</div>

<!-- fractional ownership -->
<h2 class="abs frac-title"><span>Fractional</span> jet ownership</h2>
<p class="abs frac-copy">Lorem Ipsum is simply dummy text of the printing and typesetting industry. Lorem Ipsum has been the industry's standard dummy text ever since the 1500s, when an unknown printer took a galley of type and scrambled it to make a type specimen book. It has survived not only five centuries, but also the leap into electronic typesetting, remaining essentially unchanged</p>
<div class="abs btn-outline frac-btn">View more</div>
<div class="abs jet-one" role="img" aria-label="Photo of a black private jet in side profile with white accent stripes"></div>

<!-- features -->
<div class="kicker" style="top:1148px">FEATURES</div>
<div class="abs cards">
  <article class="card">
    <svg width="80" height="60" fill="none" stroke="#22e58c" stroke-width="1.6"><path d="M8 44 L70 12 M30 34 L26 52 M48 24 L58 46 M60 17 L42 6"/></svg>
    <h3><em>JET CAR</em><br>PROGRAMS</h3>
    <p>Lorem Ipsum is simply dummy text of the printing and typesetting industry. Lorem Ipsum has been the industry's standard dummy text ever since the 1500s, when an unknown printer.</p>
  </article>
  <article class="card">
    <svg width="46" height="58" fill="none" stroke="#22e58c" stroke-width="1.6"><path d="M2 2 H32 L44 14 V56 H2 Z M32 2 V14 H44 M10 24 H36 M10 32 H36 M10 40 H36"/></svg>
    <h3><em>PRIVATE JET<br>LEASE</em> PROGRAMS</h3>
    <p>Lorem Ipsum is simply dummy text of the printing and typesetting industry. Lorem Ipsum has been the industry's standard dummy text ever since the 1500s, when an unknown printer.</p>
  </article>
  <article class="card">
    <svg width="60" height="60" fill="none" stroke="#22e58c" stroke-width="1.6"><circle cx="30" cy="30" r="10"/><circle cx="30" cy="6" r="4"/><circle cx="30" cy="54" r="4"/><circle cx="6" cy="30" r="4"/><circle cx="54" cy="30" r="4"/><circle cx="12" cy="12" r="4"/><circle cx="48" cy="48" r="4"/><circle cx="48" cy="12" r="4"/><circle cx="12" cy="48" r="4"/><path d="M25 30 L29 34 L35 26"/></svg>
    <h3><em>ALL ACCESS</em><br>PROGRAMS</h3>
    <p>Lorem Ipsum is simply dummy text of the printing and typesetting industry. Lorem Ipsum has been the industry's standard dummy text ever since the 1500s, when an unknown printer.</p>
  </article>
  <article class="card">
    <svg width="60" height="60" fill="none" stroke="#22e58c" stroke-width="1.6"><circle cx="30" cy="30" r="10"/><circle cx="30" cy="6" r="4"/><circle cx="30" cy="54" r="4"/><circle cx="6" cy="30" r="4"/><circle cx="54" cy="30" r="4"/><circle cx="12" cy="12" r="4"/><circle cx="48" cy="48" r="4"/><circle cx="48" cy="12" r="4"/><circle cx="12" cy="48" r="4"/><path d="M25 30 L29 34 L35 26"/></svg>
    <h3><em>ALL ACCESS</em><br>PROGRAMS</h3>
    <p>Lorem Ipsum is simply dummy text of the printing and typesetting industry. Lorem Ipsum has been the industry's standard dummy text ever since the 1500s, when an unknown printer.</p>
  </article>
  <article class="card">
    <svg width="50" height="62" fill="none" stroke="#22e58c" stroke-width="1.6"><rect x="2" y="4" width="18" height="26" rx="3"/><path d="M30 2 V40 H12 L8 50 H40 M14 60 H38"/></svg>
    <h3><em>SEAT CHARTER<br>FLIGHTS</em></h3>
    <p>Lorem Ipsum is simply dummy text of the printing and typesetting industry. Lorem Ipsum has been the industry's standard dummy text ever since the 1500s, when an unknown printer.</p>
  </article>
  <article class="card">
    <svg width="70" height="60" fill="none" stroke="#22e58c" stroke-width="1.6"><path d="M10 10 H66 M38 10 V20"/><rect x="20" y="20" width="34" height="22" rx="11"/><path d="M14 52 H56 M26 42 V52 M46 42 V52"/></svg>
    <h3><em>HELICOPTER</em><br>ACCESS PROGRAMS</h3>
    <p>Lorem Ipsum is simply dummy text of the printing and typesetting industry. Lorem Ipsum has been the industry's standard dummy text ever since the 1500s, when an unknown printer.</p>
  </article>
</div>

<!-- benefits -->
<section class="abs benefits">
  <h2>BENEFITS</h2>
  <p>Convenience &nbsp;|&nbsp; Luxury &nbsp;|&nbsp; Exclusivity</p>
</section>
<div class="abs jet-two" role="img" aria-label="Photo of a silver large-cabin private jet angled toward the viewer"></div>

<!-- services -->
<div class="kicker" style="top:2376px">SERVICES</div>
<div class="abs services">
  <div class="service"><h4><i></i>Dummy Service</h4><p>Lorem Ipsum is simply dummy text of the printing and typesetting industry.</p></div>
  <div class="service"><h4><i></i>Dummy Service</h4><p>Lorem Ipsum is simply dummy text of the printing and typesetting industry.</p></div>
  <div class="service"><h4><i></i>Dummy Service</h4><p>Lorem Ipsum is simply dummy text of the printing and typesetting industry.</p></div>
  <div class="service"><h4><i></i>Community Governance</h4><p>Lorem Ipsum is simply dummy text of the printing and typesetting industry.</p></div>
  <div class="service"><h4><i></i>Dummy Service</h4><p>Lorem Ipsum is simply dummy text of the printing and typesetting industry.</p></div>
  <div class="service"><h4><i></i>Dummy Service</h4><p>Lorem Ipsum is simply dummy text of the printing and typesetting industry.</p></div>
</div>

<section class="abs cta-box" style="top:2697px">
  <p>Contact SoarVane for a personalized consultation</p>
  <div class="btn">Contact Us</div>
</section>

<!-- testimonial -->
<div class="kicker" style="top:2884px">TESTIMONIAL</div>
<div class="orb" style="left:762px;top:2900px;width:160px;height:160px"></div>
<div class="orb" style="left:265px;top:3175px;width:108px;height:108px"></div>
<figure class="abs quote-card">
  <div class="quote-mark">“</div>
  <blockquote class="quote-text">If anyone is looking to create a book cover, this is the place you need to visit.My editor recommended PixelForge and I am glad she did. &nbsp;My only regret is that I didn't here about them for my first 3 books.<br>That did a great job!!</blockquote>
  <figcaption class="author"><div class="avatar" role="img" aria-label="Reviewer portrait"></div><div><b>Marlo Fenwick</b><small>Sr. Designer</small></div></figcaption>
</figure>
<div class="arrow" style="left:773px;background:#3a3b3e"><svg width="12" height="12" fill="none" stroke="#888" stroke-width="1.6"><path d="M8 2 L4 6 L8 10"/></svg></div>
<div class="arrow" style="left:830px;background:#fff"><svg width="12" height="12" fill="none" stroke="#000" stroke-width="1.6"><path d="M4 2 L8 6 L4 10"/></svg></div>

<!-- partners -->
<div class="abs brands"><span>Glimmora</span><span>Ambrosel</span><span>Nestaro</span><span>Sonique</span><span>Ventrix</span><span>Quorvo</span></div>

<!-- newsletter -->
<section class="abs newsletter">
  <h2>Newsletter</h2>
  <p>Sign up to the newsletter and learn about new resources, new commits, new proposals, and more.</p>
  <div class="email"><span>Email</span><div class="btn">SIGN UP</div></div>
</section>

<!-- faq -->
<section class="abs faq">
  <h2>FAQ’s</h2>
  <div class="faq-item" style="top:116px"><div class="q"><span>How can I pay for your logistics services?</span><svg width="12" height="8" fill="none" stroke="#22e58c" stroke-width="1.6"><path d="M1 1 L6 6 L11 1"/></svg></div><p class="a">Leverage agile frameworks to provide a robust synopsis for strategy foster collaborative thinking to further the overall value proposition. Organically grow the holistic world view of disruptive.</p></div>
  <div class="faq-item" style="top:215px"><div class="q"><span>What payment methods are supported?</span><svg width="8" height="12" fill="none" stroke="#ccc" stroke-width="1.6"><path d="M1 1 L6 6 L1 11"/></svg></div></div>
  <div class="faq-item" style="top:258px"><div class="q"><span>What options for logistics plans are available?</span><svg width="8" height="12" fill="none" stroke="#ccc" stroke-width="1.6"><path d="M1 1 L6 6 L1 11"/></svg></div></div>
  <div class="faq-item" style="top:301px"><div class="q"><span>Can I specify a delivery date when ordering?</span><svg width="8" height="12" fill="none" stroke="#ccc" stroke-width="1.6"><path d="M1 1 L6 6 L1 11"/></svg></div></div>
</section>
<div class="abs faq-visual" role="img" aria-label="Render of a white airliner under a glass dome above concentric rings"></div>

<section class="abs cta-box" style="top:4194px">
  <p>Contact SoarVane for a personalized consultation</p>
  <div class="btn">Contact Us</div>
</section>

<!-- footer -->
<footer>
  <div class="abs footer-logo">SoarVane</div>
  <nav class="abs footer-links"><span>Aircraft</span><span>Programs</span><span>Why SoarVane</span><span>Lifestyle</span><span>Sustainability</span><span>Resources</span><span>Competitors</span></nav>
  <div class="abs footer-rule"></div>
  <div class="abs footer-copy">SoarVane - All rights reserved - 2024</div>
  <div class="abs status"><i></i>Operating System</div>
  <div class="abs socials"><i></i><i></i><i></i><i></i><i></i></div>
</footer>

</body>
</html>
```